Modern and Clean Web Re-Design Project

We have 2 companies in similar industries: Printing and Mail Preparation/Fulfillment. We prefer sites that are clean and easy to navigate.Our printing company, Harbourline Press Works' website, hpwgroup-example.ca is outdated needs revamping. We have rebranded our logo and are looking for a new design that is clean, modern and geared to other corporations and business in the downtown Toronto area. Our mailing company, The Parcel Loft (theparcelloft-example.ca) needs a website as well. This company is in the Direct Mail and letter shop business, which essentially is addressing/personalizing people's printed matter and preparing it for either the Canadian or US postal service. The Parcel Loft specializes in not-for-profit and corporate sectors.Please see our logos to get an idea of the colors and look we want. For all intensive purposes, the sites can look similar in design all we want is that each site has the appropriate corporate colors and is a bit different so they don't look identical as the two business run as separate corporations.The content of the website should be easily changed by our staff and we want it to be setup to optimized for SEO based on the keywords we want. We are looking for someone to work on this project immediately

After doing some thinking, I would like the site to be more modern but the non flash sites that I have seen so far Im finding life-less and while I want something clean, not overly busy and corporate looking, I dont want the design to be bland looking.

Please design with the previous specs in mind but with a twist as mentioned above.

Thanks
Dorian

Target Market(s)

See above

Industry/Entity Type

Printing

Requirements
Must have
• Must match the design and style of each respective logoSee the attached impage of the front of our offices to have an idea of our lookWe must be able to edit the content ourselves without any fancy programs or tools.Must be SEO optimized
Nice to have
• An online order form that can be emailed to us for quotes.....perhaps a page with a bunch of fields that have drop down menus....
Should not have
• Should not be overly busy. I want it to be clean and simple but informative without being hard to navigate

```html
<!DOCTYPE html>
<html lang="en">
<head>
<meta charset="utf-8">
<title>Harbourline Press Works — Digital Printing</title>
<link rel="stylesheet" href="https://fonts.googleapis.com/css2?family=Glegoo&family=Raleway:wght@400;500&family=Orbitron:wght@900&family=Michroma&display=swap">
<style>
:root{
  --orange:#f15a3a;
  --amber:#fbb12f;
  --brown:#a8835c;
  --ink:#3d3d3d;
  --paper:#fbfbfa;
  --grey:#c9c9c9;
  --white:#ffffff;
}
*{box-sizing:border-box;margin:0;padding:0}
html,body{width:1200px;height:1192px;overflow:hidden}
body{position:relative;background:var(--paper);font-family:"Glegoo",serif;color:var(--ink)}
.stripe{position:absolute;left:0;top:0;width:1200px;height:8px;
  background:repeating-linear-gradient(90deg,var(--orange) 0 38px,var(--amber) 38px 72px,var(--brown) 72px 110px,var(--amber) 110px 150px)}
.header{position:absolute;left:0;top:8px;width:1200px;height:87px;background:var(--white)}
.brand{position:absolute;left:120px;top:28px;display:flex;align-items:center;gap:10px;
  font-family:"Raleway",sans-serif;font-weight:500;font-size:19px;color:var(--orange)}
.brand-dot{width:14px;height:14px;border-radius:50%;background:var(--amber)}
.contact{position:absolute;right:128px;top:22px;display:flex;align-items:center;gap:10px;
  font-family:"Raleway",sans-serif;font-size:14px;color:var(--ink)}
.contact svg{display:block}
.contact .sep{color:var(--brown)}
.social{display:flex;gap:6px;margin-left:12px}
.social span{width:20px;height:20px;border-radius:50%;background:var(--brown)}
.nav{position:absolute;right:63px;top:54px;display:flex;gap:0;list-style:none;
  font-family:"Raleway",sans-serif;font-size:16px;color:var(--orange)}
.nav li{padding:0 22px}
.header-rule{position:absolute;left:0;top:94px;width:1200px;height:8px;background:var(--amber)}
.nav-active{position:absolute;left:575px;top:94px;width:132px;height:7px;background:var(--orange)}
.hero{position:absolute;left:0;top:102px;width:1200px;height:358px;background:var(--white)}
.hero-mosaic{position:absolute;left:0;bottom:0;width:1200px;height:150px;
  background:linear-gradient(180deg,rgba(201,201,201,0) 0%,#d6d6d6 45%,var(--grey) 100%)}
.hero-photo{position:absolute;left:160px;top:33px;width:580px;height:305px;border-radius:14px 14px 6px 6px;
  background:linear-gradient(180deg,#3b3b3b 0%,#5a5a5a 30%,#b0567e 55%,#5e7d3e 100%)}
.hero-title{position:absolute;left:798px;top:92px;text-align:left}
.hero-title .big{font-family:"Orbitron",sans-serif;font-weight:900;font-size:48px;letter-spacing:2px;color:#111;line-height:1}
.hero-title .small{font-family:"Michroma",sans-serif;font-size:32px;letter-spacing:8px;color:#111;margin-top:10px;line-height:1}
.steps{position:absolute;left:0;top:470px;width:1200px}
.step{position:absolute;top:0;width:300px;text-align:center}
.step-circle{position:absolute;top:27px;width:164px;height:164px;border-radius:50%;background:var(--amber)}
.step-num{position:absolute;top:28px;width:56px;height:56px;border-radius:50%;background:#ef4b36;
  color:var(--white);font-family:"Raleway",sans-serif;font-size:34px;line-height:56px;text-align:center}
.step-icon{position:absolute}
.step h2{position:absolute;top:202px;left:0;width:300px;font-weight:400;font-size:24px;color:var(--ink)}
.step p{position:absolute;top:255px;left:18px;width:264px;font-size:14.5px;line-height:21.6px;color:var(--ink)}
.arrow{position:absolute;top:548px}
.footer{position:absolute;left:0;top:956px;width:1200px;height:228px;background:var(--brown);color:var(--white)}
.footer h3{font-family:"Raleway",sans-serif;font-weight:400;font-size:18px;letter-spacing:.5px;margin-bottom:16px}
.about{position:absolute;left:120px;top:24px;width:310px;font-family:"Raleway",sans-serif;font-size:13px;line-height:18.8px}
.services{position:absolute;left:532px;top:24px;font-family:"Raleway",sans-serif;font-size:13.5px;line-height:22.5px;list-style:none}
.footer-brand{position:absolute;left:850px;top:62px;width:230px;text-align:right}
.footer-brand .name{display:flex;align-items:center;justify-content:flex-end;gap:10px;
  font-family:"Raleway",sans-serif;font-weight:500;font-size:21px;color:var(--white)}
.footer-brand .name span{width:14px;height:14px;border-radius:50%;background:var(--white)}
.copyright{margin-top:38px;font-family:Arial,sans-serif;font-size:12.5px;line-height:18.8px;font-weight:bold}
.bottom-band{position:absolute;left:0;top:1184px;width:1200px;height:8px;background:var(--amber)}
</style>
</head>
<body>
<div class="stripe"></div>

<header class="header">
  <div class="brand"><span class="brand-dot"></span>Harbourline Press Works</div>
  <div class="contact">
    <svg width="18" height="14" viewBox="0 0 18 14"><path d="M1 5 L9 1 L17 5 V13 H1 Z M1 5 L9 10 L17 5" fill="none" stroke="#a8835c" stroke-width="1.8"/></svg>
    <span>info@hpwgroup-example.ca</span>
    <span class="sep">|</span>
    <svg width="16" height="16" viewBox="0 0 16 16"><path d="M3 1 L6 4 L4.5 6 Q6.5 9.5 10 11.5 L12 10 L15 13 L12.5 15 Q5 13.5 1 3.5 Z" fill="#a8835c"/></svg>
    <span>416-555-0148</span>
    <div class="social"><span></span><span></span></div>
  </div>
  <ul class="nav">
    <li>Who are we</li>
    <li>What do we do</li>
    <li>Email a file</li>
    <li>Contact us</li>
  </ul>
</header>
<div class="header-rule"></div>
<div class="nav-active"></div>

<section class="hero">
  <div class="hero-mosaic" role="img" aria-label="Soft grey pixel mosaic backdrop"></div>
  <div class="hero-photo" role="img" aria-label="Wide-format digital printer producing a large floral print"></div>
  <div class="hero-title">
    <div class="big">DIGITAL</div>
    <div class="small">PRINTING</div>
  </div>
</section>

<section class="steps">
  <div class="step" style="left:99px">
    <div class="step-circle" style="left:68px"></div>
    <div class="step-num" style="left:50px">1</div>
    <svg class="step-icon" style="left:112px;top:63px" width="76" height="94" viewBox="0 0 76 94">
      <rect x="2" y="8" width="72" height="84" fill="#fff" stroke="#3d3d3d" stroke-width="3"/>
      <rect x="22" y="2" width="32" height="12" rx="4" fill="#fff" stroke="#3d3d3d" stroke-width="3"/>
      <circle cx="38" cy="6" r="2.5" fill="#3d3d3d"/>
    </svg>
    <h2>order &amp; send file</h2>
    <p>Lorem ipsum dolor sit amet elit, sed do eiusmod tempor incididunt ut labore et dolore magna aliqua. Ut ea commodo consequat. Duis aute irure dolor in reprehenderit in cillum dolore pariatur. Excepteur sint non proident deserunt mollit anim est commodo consequat laborum.</p>
  </div>

  <div class="step" style="left:448px">
    <div class="step-circle" style="left:68px"></div>
    <div class="step-num" style="left:68px">2</div>
    <svg class="step-icon" style="left:106px;top:76px" width="92" height="80" viewBox="0 0 92 80">
      <rect x="2" y="2" width="88" height="76" rx="14" fill="#fff" stroke="#3d3d3d" stroke-width="3.5"/>
      <path d="M12 64 L30 44 L38 52 L56 28 L78 64 Z" fill="#3d3d3d"/>
    </svg>
    <h2 style="top:198px">print</h2>
    <p>Lorem ipsum dolor sit amet elit, sed do eiusmod tempor incididunt ut labore et dolore magna aliqua. Ut ea commodo consequat. Duis aute irure dolor in reprehenderit in cillum dolore pariatur. Excepteur sint non proident deserunt mollit anim est commodo consequat laborum.</p>
  </div>

  <div class="step" style="left:799px">
    <div class="step-circle" style="left:68px"></div>
    <div class="step-num" style="left:68px">3</div>
    <svg class="step-icon" style="left:113px;top:64px" width="78" height="90" viewBox="0 0 78 90">
      <rect x="3" y="3" width="72" height="70" rx="12" fill="#fff" stroke="#3d3d3d" stroke-width="4"/>
      <path d="M39 3 V73 M3 36 H75" stroke="#3d3d3d" stroke-width="4"/>
      <circle cx="16" cy="82" r="6" fill="#fff" stroke="#3d3d3d" stroke-width="3"/>
      <circle cx="62" cy="82" r="6" fill="#fff" stroke="#3d3d3d" stroke-width="3"/>
    </svg>
    <h2 style="top:198px">delivery</h2>
    <p>Lorem ipsum dolor sit amet elit, sed do eiusmod tempor incididunt ut labore et dolore magna aliqua. Ut ea commodo consequat. Duis aute irure dolor in reprehenderit in cillum dolore pariatur. Excepteur sint non proident deserunt mollit anim est commodo consequat laborum.</p>
  </div>
</section>

<svg class="arrow" style="left:386px" width="96" height="64" viewBox="0 0 96 64">
  <path d="M2 22 L62 18 L60 4 L94 30 L64 60 L64 44 L4 42 Z" fill="#fff" stroke="#3d3d3d" stroke-width="2.5" stroke-linejoin="round"/>
  <path d="M6 38 L60 40" stroke="#3d3d3d" stroke-width="3" stroke-dasharray="2 2"/>
</svg>
<svg class="arrow" style="left:735px" width="96" height="64" viewBox="0 0 96 64">
  <path d="M2 22 L62 18 L60 4 L94 30 L64 60 L64 44 L4 42 Z" fill="#fff" stroke="#3d3d3d" stroke-width="2.5" stroke-linejoin="round"/>
  <path d="M6 38 L60 40" stroke="#3d3d3d" stroke-width="3" stroke-dasharray="2 2"/>
</svg>

<footer class="footer">
  <div class="about">
    <h3>ABOUT HPW</h3>
    <p>We maintain absolute integrity in every aspect of our operation. By using our experience to understand our customers' expectations, we show an uncommon commitment to achieving a high-quality product under strict deadlines. It is the customers who set the standards we strive to achieve. We are professionals who bring unique and specialized skills you can depend on.</p>
  </div>
  <ul class="services">
    <li><h3 style="margin-bottom:10px">OUR SERVICES</h3></li>
    <li>Digital Printing</li>
    <li>Commercial Printing</li>
    <li>Legal Services</li>
    <li>Parcel Loft</li>
    <li>Computer Services</li>
    <li>Free Pick Up and Delivery</li>
  </ul>
  <div class="footer-brand">
    <div class="name"><span></span>Harbourline Press Works</div>
    <p class="copyright">copyright (c) HPW Online 2013<br>all rights reserved</p>
  </div>
</footer>
<div class="bottom-band"></div>
</body>
</html>
```